ALL TEXT GRAPHICS RK May 2025 for Instagram

We are looking for a series of social media graphics for Instagram (new size: 4:5 (1080 x 1350 pixels) ratio that are ALL TEXT. We want the following quotes below on each graphic; one quote per graphic. AND, In very small letters at the bottom of each graphic, add @RKBexleyOnline
The look and feel of these graphics should be complimentary to the color palette attached below; but keep them simple. But the design is up to you; at the end of this document, I provided various samples of all text graphics that I like as examples.
women looking to lose weight

```html
<!DOCTYPE html>
<html lang="en">
<head>
<meta charset="utf-8">
<title>RK Instagram Text Graphics</title>
<link rel="stylesheet" href="https://fonts.googleapis.com/css2?family=Fraunces:opsz,wght@9..144,500;9..144,700&family=Italiana&display=swap">
<style>
  :root {
    --pink: #ee1a8a;
    --ink: #1a1a1a;
    --paper: #ffffff;
    --frame: #111111;
  }
  * { margin: 0; padding: 0; box-sizing: border-box; }
  html, body { width: 960px; height: 1200px; overflow: hidden; background: var(--paper); }
  .sheet { position: relative; width: 960px; height: 1200px; }
  .card {
    position: absolute;
    width: 273px;
    height: 367px;
    border: 1.5px solid var(--frame);
    background: var(--paper);
    overflow: hidden;
  }
  .card--featured { border-width: 3px; }
  .card > * { position: absolute; left: 19px; right: 8px; }
  .lede {
    font-family: "Fraunces", Georgia, serif;
    font-weight: 500;
    font-size: 20px;
    line-height: 1.25;
    letter-spacing: -0.04em;
    color: var(--pink);
  }
  .body {
    font-family: "Italiana", "Didot", serif;
    font-size: 24px;
    line-height: 1.28;
    color: var(--pink);
    text-transform: uppercase;
    white-space: nowrap;
  }
  .body--small { font-size: 19px; line-height: 1.32; }
  .body strong { font-family: "Fraunces", Georgia, serif; font-weight: 700; font-size: 0.88em; }
  .hero {
    font-family: "Italiana", "Didot", serif;
    font-size: 42px;
    line-height: 1;
    color: var(--ink);
    text-transform: uppercase;
    letter-spacing: -0.03em;
    white-space: nowrap;
  }
  .sparkle { display: inline-block; width: 22px; height: 22px; vertical-align: top; margin-top: -8px; }
  .rule { top: 320px; width: 30px; height: 1.5px; background: var(--pink); right: auto; }
  .handle {
    top: 334px;
    font-family: "Fraunces", Georgia, serif;
    font-weight: 500;
    font-size: 12px;
    letter-spacing: -0.03em;
    color: var(--pink);
  }
  .center { text-align: center; left: 8px; }
  .rule.center { left: 121px; }
</style>
</head>
<body>
<svg width="0" height="0" style="position:absolute">
  <defs>
    <symbol id="spark" viewBox="0 0 24 24">
      <path d="M12 2 L13.4 10.6 L22 12 L13.4 13.4 L12 22 L10.6 13.4 L2 12 L10.6 10.6 Z" fill="#ee1a8a"/>
      <path d="M4 3 L4.5 5 L6 5.5 L4.5 6 L4 8 L3.5 6 L2 5.5 L3.5 5 Z" fill="#ee1a8a"/>
      <circle cx="21" cy="20" r="0.9" fill="#ee1a8a"/>
    </symbol>
  </defs>
</svg>
<main class="sheet">

  <section class="card" style="left:53px;top:29px">
    <p class="lede" style="top:28px">Bloating.<br>Muffin top.<br>Puffy waistline</p>
    <p class="body" style="top:115px">Your body’s<br>screaming for<br>a different kind<br>of fix.</p>
    <p class="hero" style="top:262px;font-size:44px">Here it is<svg class="sparkle"><use href="#spark"/></svg></p>
    <span class="rule"></span><p class="handle">@RKBexleyOnline</p>
  </section>

  <section class="card" style="left:343px;top:29px">
    <p class="lede" style="top:36px">Flat tummy<br>in your 40s?</p>
    <p class="hero" style="top:116px;font-size:46px">It’s still<br>possible !<svg class="sparkle"><use href="#spark"/></svg></p>
    <p class="body body--small" style="top:234px">Comment <strong>Bye Belly</strong> to<br>get the 10 secrets to<br>a flatter tummy</p>
    <span class="rule"></span><p class="handle">@RKBexleyOnline</p>
  </section>

  <section class="card" style="left:633px;top:29px">
    <p class="lede" style="top:41px">The stubborn belly fat<br>after 40?</p>
    <p class="body" style="top:112px">It’s not about<br>calories,<br>it’s about your<br>hormones.</p>
    <p class="hero" style="top:266px;font-size:31px">Here is the fix !<svg class="sparkle"><use href="#spark"/></svg></p>
    <span class="rule"></span><p class="handle">@RKBexleyOnline</p>
  </section>

  <section class="card" style="left:53px;top:416px">
    <p class="lede" style="top:41px">Your belly isn’t fat...<br>it’s hormonal</p>
    <p class="hero" style="top:130px;left:14px;font-size:39px">And here’s<br>how to fix it<svg class="sparkle"><use href="#spark"/></svg></p>
    <p class="body body--small" style="top:240px;left:14px">Comment <strong>Hormones</strong> if<br>nothing is working.</p>
    <span class="rule"></span><p class="handle">@RKBexleyOnline</p>
  </section>

  <section class="card card--featured" style="left:343px;top:416px">
    <p class="lede" style="top:38px">This 90-day plan<br>helped women over 40<br>slim down,</p>
    <p class="body" style="top:131px">Get a tiny waist<br>and feel sexy<br>again.</p>
    <p class="hero" style="top:254px;font-size:40px">You’re next.<svg class="sparkle"><use href="#spark"/></svg></p>
    <span class="rule"></span><p class="handle">@RKBexleyOnline</p>
  </section>

  <section class="card" style="left:633px;top:416px">
    <p class="lede" style="top:38px">What worked in your<br>30s won’t work now.</p>
    <p class="body" style="top:109px">Here’s what<br>actually does</p>
    <p class="hero" style="top:188px;font-size:40px">Drop<br>30 pounds<svg class="sparkle"><use href="#spark"/></svg><br>in 3 months.</p>
    <span class="rule"></span><p class="handle">@RKBexleyOnline</p>
  </section>

  <section class="card" style="left:53px;top:803px">
    <p class="lede" style="top:33px">That stubborn weight?<br>It’s not your fault.</p>
    <p class="body" style="top:113px">Your hormones<br>are to blame and<br>you’re not alone</p>
    <p class="hero center" style="top:236px;font-size:40px">But there is<br>a fix.<svg class="sparkle"><use href="#spark"/></svg></p>
    <span class="rule center"></span><p class="handle center">@RKBexleyOnline</p>
  </section>

  <section class="card" style="left:343px;top:803px">
    <p class="lede" style="top:26px">Tired.<br>Moody.<br>Stubborn Belly Fat</p>
    <p class="body" style="top:124px;font-size:26px">Your hormones<br>are screaming<br>for help!</p>
    <p class="hero" style="top:268px;font-size:35px">Let’s fix that.<svg class="sparkle"><use href="#spark"/></svg></p>
    <span class="rule"></span><p class="handle">@RKBexleyOnline</p>
  </section>

  <section class="card" style="left:633px;top:803px">
    <p class="lede" style="top:30px">This is the secret<br>women over 40 are<br>using to get snatched</p>
    <p class="hero" style="top:132px">Without<br>starving.<svg class="sparkle"><use href="#spark"/></svg></p>
    <p class="body body--small" style="top:254px">Comment <strong>Skinny</strong><br>to get the exact plan.</p>
    <span class="rule"></span><p class="handle">@RKBexleyOnline</p>
  </section>

</main>
</body>
</html>
```